Business Card Design Project

Colette Marivaux logo on front of card with 'of Sydney' added in small font.
Back of card needs to include the following information :

"Pure pleasure for the discerning gentleman" (I may omit once I've seen the design)

colettemarivaux.com.au

Contact by SMS or email only :

colette@colettemarivaux.com.au
Mobile : 0483 956 204 or + 61 483 956 204

Target Market(s)

Male professionals aged 20-60.

Industry/Entity Type

Business

Requirements
Must have
• Simple, bold, stylish and elegant.

```html
<!DOCTYPE html>
<html lang="en">
<head>
<meta charset="utf-8">
<title>Colette Marivaux of Sydney – Business Card</title>
<link rel="stylesheet" href="https://fonts.googleapis.com/css2?family=Questrial&display=swap">
<style>
  :root {
    --ink-night: #0d0f14;
    --ink-black: #000000;
    --paper: #ffffff;
    --seam: #f3efea;
    --text-dark: #1a1a1a;
    --text-light: #ffffff;
    --text-muted: #d9d9d9;
    --rule: #3a3a3a;
  }
  * { margin: 0; padding: 0; box-sizing: border-box; }
  html, body {
    width: 981px;
    height: 1200px;
    overflow: hidden;
    background: var(--paper);
  }
  .card {
    position: relative;
    width: 981px;
    height: 1200px;
    font-family: "Questrial", "Helvetica Neue", Arial, sans-serif;
    color: var(--text-dark);
    background: var(--paper);
  }
  .front-band-upper {
    position: absolute; left: 0; top: 0;
    width: 981px; height: 330px;
    background: var(--ink-night);
  }
  .front-band-lower {
    position: absolute; left: 0; top: 330px;
    width: 981px; height: 261px;
    background: var(--ink-black);
  }
  .seam {
    position: absolute; left: 0; top: 591px;
    width: 981px; height: 9px;
    background: var(--seam);
  }
  .brand-name {
    position: absolute; left: 0; top: 228px;
    width: 981px;
    text-align: center;
    font-size: 62px;
    font-weight: 400;
    letter-spacing: 2px;
    color: var(--text-light);
    line-height: 1;
  }
  .brand-locale {
    position: absolute; right: 386px; top: 373px;
    font-size: 18px;
    letter-spacing: 1px;
    color: var(--text-muted);
    line-height: 1;
  }
  .tagline {
    position: absolute; left: 0; top: 706px;
    width: 981px;
    text-align: center;
    font-size: 37px;
    line-height: 1;
    letter-spacing: -0.3px;
  }
  .tagline-rule {
    position: absolute; left: 0; top: 758px;
    width: 981px; height: 1px;
    background: var(--rule);
  }
  .contact {
    position: absolute; right: 49px; top: 918px;
    text-align: right;
    font-size: 30px;
    line-height: 1;
  }
  .contact .website {
    display: inline-block;
    color: var(--text-dark);
    text-decoration: underline;
    text-decoration-thickness: 1px;
    text-underline-offset: 6px;
    margin-right: -2px;
  }
  .contact .note { margin-top: 45px; }
  .contact .email { margin-top: 45px; }
  .contact .mobile { margin-top: 7px; }
</style>
</head>
<body>
  <main class="card">
    <div class="front-band-upper"></div>
    <div class="front-band-lower"></div>
    <div class="seam"></div>

    <div class="brand-name">Colette Marivaux</div>
    <div class="brand-locale">of Sydney</div>

    <p class="tagline">Pure pleasure for the discerning gentleman</p>
    <div class="tagline-rule"></div>

    <section class="contact">
      <a class="website">colettemarivaux.com.au</a>
      <p class="note">Contact by SMS or email only :</p>
      <p class="email">colette@colettemarivaux.com.au</p>
      <p class="mobile">Mobile : 0483 956 204 or + 61 483 956 204</p>
    </section>
  </main>
</body>
</html>
```